Plivora Design Project

I need new cover graphics for my father's plivora page. He is running for major of our town in Puerto Rico.
Need his name on the cover: Mateo Brunal
And the position, town and year: Alcalde Carolina 2012
As a default background color you can use the blue in the current cover graphic, or go here for color ideas http://www.lumbrevecinal2012.com/indexContinuar.php
I really would like to see something that incorporates some of the pictures I have uploaded of him with people in the town, or with popular leaders. He is the guy with gray hair.
Below is the target plivora page. Thanks
https://www.plivora.com/mateobrunal.quesada

```html
<!DOCTYPE html>
<html lang="es">
<head>
<meta charset="utf-8">
<title>Mateo Brunal · Alcalde Carolina 2012</title>
<link rel="stylesheet" href="https://fonts.googleapis.com/css2?family=Lobster&family=Oswald:wght@600&display=swap">
<style>
  :root {
    --sky-deep: #0b5fa8;
    --sky-mid: #1583cf;
    --sky-light: #3eaae8;
    --flag-blue: #2f4a98;
    --flag-red: #e3202a;
    --flag-red-dark: #b5161f;
    --white: #ffffff;
    --portrait-light: #e9eef2;
    --portrait-mid: #b9c3cc;
  }
  * { margin: 0; padding: 0; box-sizing: border-box; }
  html, body { width: 1200px; height: 444px; overflow: hidden; background: var(--white); }
  .cover {
    position: relative;
    width: 1200px;
    height: 444px;
    overflow: hidden;
    background:
      radial-gradient(ellipse 520px 260px at 700px 160px, var(--sky-light) 0%, rgba(62,170,232,0) 100%),
      linear-gradient(180deg, var(--sky-mid) 0%, var(--sky-mid) 45%, var(--sky-deep) 100%);
  }
  .flag { position: absolute; left: 0; top: 0; }
  .office-label {
    position: absolute;
    width: 200px;
    text-align: center;
    left: 268px;
    font-family: "Lobster", cursive;
    font-size: 36px;
    color: var(--white);
    text-shadow: 1px 2px 3px rgba(0,0,0,0.35);
    line-height: 1;
  }
  .office-title { top: 79px; }
  .office-town { top: 201px; }
  .office-year { top: 323px; }
  .portrait {
    position: absolute;
    left: 872px;
    top: 40px;
    width: 328px;
    height: 404px;
    border-radius: 164px 164px 0 0;
    background: radial-gradient(ellipse at 50% 40%, var(--portrait-light) 0%, var(--portrait-mid) 70%, rgba(185,195,204,0) 100%);
  }
  .candidate-name {
    position: absolute;
    z-index: 2;
    left: 488px;
    top: 100px;
    width: 370px;
    text-align: center;
    color: var(--white);
    text-shadow: 2px 4px 6px rgba(0,0,0,0.35);
  }
  .name-first {
    display: block;
    font-family: "Lobster", cursive;
    font-size: 104px;
    line-height: 1;
  }
  .name-last {
    display: block;
    font-family: "Oswald", sans-serif;
    font-weight: 600;
    font-size: 110px;
    line-height: 1;
    margin-top: -2px;
    letter-spacing: 0;
  }
</style>
</head>
<body>
  <main class="cover">
    <svg class="flag" width="480" height="444" viewBox="0 0 480 444" aria-hidden="true">
      <defs>
        <linearGradient id="bandShade" x1="0" y1="0" x2="0" y2="1">
          <stop offset="0" stop-color="var(--flag-red)"/>
          <stop offset="1" stop-color="var(--flag-red-dark)"/>
        </linearGradient>
      </defs>
      <polygon class="band" points="0,51 434,51 471,100 434,148 0,148" fill="url(#bandShade)"/>
      <polygon class="band" points="0,173 434,173 471,222 434,270 0,270" fill="url(#bandShade)"/>
      <polygon class="band" points="0,295 434,295 471,344 434,392 0,392" fill="url(#bandShade)"/>
      <polygon class="flag-triangle" points="0,0 273,222 0,444" fill="var(--flag-blue)"/>
      <polygon class="flag-star" fill="var(--white)"
        points="116,150 133,199 185,200 144,231 159,280 116,251 73,280 88,231 47,200 99,199"/>
    </svg>

    <div class="office-label office-title">Alcalde</div>
    <div class="office-label office-town">Carolina</div>
    <div class="office-label office-year">2012</div>

    <div class="portrait" role="img" aria-label="Portrait photograph of the candidate, a gray-haired man in a striped shirt"></div>

    <h1 class="candidate-name">
      <span class="name-first">Mateo</span>
      <span class="name-last">BRUNAL</span>
    </h1>
  </main>
</body>
</html>
```